Veltro Coaching Business Card

We need a business card designed for a a company called "Veltro Coaching". We offer consulting, coaching and training to business leaders and coaches (across the world) using the latest findings in neuroscience, social and emotional intelligence and positive psychology. The final design should communicate the use of brain science to create sustainable relationships.

The card should be doublesided. The logo is attached and names and titles will be provided to the successful designer. Thank you.

Industry/Entity Type

Training

```html
<!DOCTYPE html>
<html lang="en">
<head>
<meta charset="utf-8">
<title>Veltro Coaching Business Card</title>
<link rel="stylesheet" href="https://fonts.googleapis.com/css2?family=Questrial&display=swap">
<style>
  :root {
    --teal: #02c4c6;
    --teal-deep: #12b6c2;
    --lime: #b9ff1c;
    --white: #ffffff;
    --page: #ffffff;
    --border: #7fdde3;
  }
  * { margin: 0; padding: 0; box-sizing: border-box; }
  html, body {
    width: 850px; height: 1200px; overflow: hidden;
    background: var(--page);
    font-family: "Questrial", Arial, sans-serif;
  }
  .canvas { position: relative; width: 850px; height: 1200px; }

  /* Front side */
  .card-front {
    position: absolute; left: 0; top: 0;
    width: 850px; height: 508px;
    background: var(--teal);
    border-radius: 26px;
    overflow: hidden;
    color: var(--white);
  }
  .holder-name {
    position: absolute; left: 92px; top: 98px;
    font-size: 37px; font-weight: 400; letter-spacing: 0.5px;
  }
  .holder-position {
    position: absolute; left: 92px; top: 152px;
    font-size: 21px;
  }
  .contact-row {
    position: absolute; left: 84px;
    display: flex; align-items: center;
    font-size: 24px; letter-spacing: 0.5px;
  }
  .contact-row svg { width: 36px; height: 36px; flex: none; }
  .contact-row .sep { position: absolute; left: 62px; top: -8px; font-size: 20px; }
  .contact-row .value { position: absolute; white-space: nowrap; }
  .row-mobile { top: 284px; }
  .row-phone { top: 343px; }
  .row-mail { top: 400px; }
  .row-mobile .value, .row-phone .value { left: 153px; }
  .row-mail .value { left: 98px; }

  .profile-art {
    position: absolute; left: 585px; top: 29px;
    width: 265px; height: 415px;
    border-radius: 120px 0 0 70px;
    background: linear-gradient(100deg, var(--lime) 0%, #e9ffd0 18%, var(--white) 32%, var(--white) 100%);
  }

  /* Back side */
  .card-back {
    position: absolute; left: 5px; top: 694px;
    width: 844px; height: 502px;
    background: var(--white);
    border: 1.5px solid var(--border);
    border-radius: 32px;
  }
  .brand {
    position: absolute; left: 0; right: 0; top: 150px;
    display: flex; justify-content: center; align-items: center; gap: 22px;
  }
  .brand-dot {
    width: 64px; height: 64px; border-radius: 50%;
    background: var(--teal);
  }
  .brand-name {
    font-size: 60px; color: var(--teal); letter-spacing: 1px;
  }
  .web-address {
    position: absolute; left: 0; right: 0; top: 366px;
    text-align: center; font-size: 35px; color: var(--teal-deep);
    letter-spacing: 0.5px;
  }
</style>
</head>
<body>
<main class="canvas">

  <section class="card-front" aria-label="Card front">
    <h1 class="holder-name">Your Name</h1>
    <p class="holder-position">Position</p>

    <div class="contact-row row-mobile">
      <svg viewBox="0 0 36 36" fill="none" stroke="#fff" stroke-width="1.8" aria-hidden="true">
        <rect x="10" y="3" width="16" height="30" rx="3"/>
        <rect x="13" y="7" width="10" height="12"/>
        <line x1="14" y1="24" x2="22" y2="24"/><line x1="14" y1="28" x2="22" y2="28"/>
      </svg>
      <span class="sep">:</span>
      <span class="value">+60 12 555 0147</span>
    </div>

    <div class="contact-row row-phone">
      <svg viewBox="0 0 36 36" fill="none" stroke="#fff" stroke-width="1.8" aria-hidden="true">
        <path d="M11 4 L15 10 L12 14 C13 19 17 24 21 26 L25 23 L31 27 L28 32 C18 31 6 19 5 8 Z"/>
      </svg>
      <span class="sep">:</span>
      <span class="value">+60 12 555 0147</span>
    </div>

    <div class="contact-row row-mail">
      <svg viewBox="0 0 36 36" fill="none" stroke="#fff" stroke-width="1.8" aria-hidden="true">
        <rect x="2" y="9" width="32" height="20"/>
        <polyline points="2,9 18,21 34,9"/>
      </svg>
      <span class="sep">:</span>
      <span class="value">hello@veltro.example</span>
    </div>

    <div class="profile-art" role="img" aria-label="Illustration of a head in profile in white with a lime offset"></div>
  </section>

  <section class="card-back" aria-label="Card back">
    <div class="brand">
      <span class="brand-dot" aria-hidden="true"></span>
      <span class="brand-name">Veltro Coaching</span>
    </div>
    <p class="web-address">www.veltro.example</p>
  </section>

</main>
</body>
</html>
```